Non-Profit needs enticing Winter Advertisement

The Alliance for a Clearwater Valley (ACWV) is looking to create a dynamic advertising campaign highlighting exciting winter activities in NH. We will also be incorporating drug prevention messaging into these ads.
ACWV is a nonprofit organization that strives to create and promote consistent statewide messages about the problems and solutions of substance misuse in New Hampshire through engagement. We want to highlight the importance of talking to children/teens about the challenges of drug use through the winter.

Our website is here: http://clearwatervalley-alliance.org/
Our Facebook page is here:https://www.facebook.com/ClearwaterValleyAlliance/

Target Market(s)

Young adults + Parents with kids.

Industry/Entity Type

Government Health Service

Font styles to use
Sans Serif

Colors

Designer to choose colors to be used in the design.

Requirements
Must have
• Please design 1 full-page advertisement with the following idea:
• Image - a family outside skiing/snowboarding, or a mother + son/daughter skiing/snowboarding, or a father + son/daughter skiing/snowboarding
• Text options:
• Start prevention on the bunny hill. Have a conversation with your teen about staying safe this season and all year round.
• Don't let conversations about drugs and alcohol go downhill fast. Take the time to talk with your kids about drugs and alcohol regularly.
• -Something along these lines - a small pun about skiing/winter/cold and then a reminder to start a prevention conversation. If you have a creative idea throw it out there!
• We want to see a colored box at the bottom for more text and logos. Please use the attached photos for inspiration - but again if you think something would look AMAZING you have the freedom to impress us!
Nice to have
• Lato is typically our brand font.
Should not have
• This is not meant to be a scare tactic ad. This is to be a family friendly reminder of bringing the family together/

```html
<!DOCTYPE html>
<html lang="en">
<head>
<meta charset="utf-8">
<title>Start Prevention on the Bunny Hill – The Alliance for a Clearwater Valley</title>
<link href="https://fonts.googleapis.com/css2?family=Lato:wght@400;700;900&display=swap" rel="stylesheet">
<style>
  :root{
    --navy:#1f2f6e;
    --yellow:#f6e63a;
    --band-blue:#4f88cc;
    --sky-top:#9bb8dc;
    --sky-bottom:#5f7fa8;
    --white:#ffffff;
    --stage:#ececec;
  }
  *{box-sizing:border-box;margin:0;padding:0}
  html,body{width:1200px;height:542px;overflow:hidden;background:var(--stage);font-family:"Lato",sans-serif}
  .ad{position:absolute;left:408px;top:0;width:384px;height:542px;overflow:hidden;background:var(--yellow)}
  .ad-shapes{position:absolute;inset:0;width:384px;height:542px}
  .brand{position:absolute;right:0;top:0;width:190px;height:54px;background:var(--white);display:flex;align-items:center;justify-content:center;padding:0 12px;text-align:center}
  .brand-name{font-weight:900;font-size:13px;line-height:1.15;color:var(--navy)}
  .pun{position:absolute;left:206px;top:80px;width:178px;text-align:center;color:var(--yellow);font-weight:900;line-height:.98;
       text-shadow:0 0 2px var(--navy),1px 1px 0 var(--navy),-1px -1px 0 var(--navy),1px -1px 0 var(--navy),-1px 1px 0 var(--navy)}
  .pun-small{font-size:16px;font-weight:700;display:block}
  .pun-big{font-size:44px;display:block}
  .pun-mid{font-size:25px;display:block}
  .pun-mid small{font-size:17px;font-weight:700}
  .pun-prev{font-size:27px;display:block}
  .pun-conv{font-size:19px;display:block}
  .lead{position:absolute;left:12px;top:304px;width:206px;text-align:center;color:var(--navy)}
  .lead-title{font-weight:900;font-size:25px;line-height:.95}
  .lead-text{font-size:12.5px;line-height:1.15;margin:5px auto 0;width:192px}
  .talk{position:absolute;right:12px;top:278px;width:128px;text-align:right;color:var(--white);font-size:12.5px;line-height:1.3}
  .contact{position:absolute;left:12px;top:524px;font-size:10px;font-weight:700;color:var(--navy);white-space:nowrap}
  .web{position:absolute;right:12px;top:522px;font-size:11.5px;font-weight:700;color:var(--white);white-space:nowrap}
</style>
</head>
<body>
<main class="ad">
  <svg class="ad-shapes" viewBox="0 0 384 542">
    <defs>
      <linearGradient id="sky" x1="0" y1="0" x2="0" y2="1">
        <stop offset="0" stop-color="#9bb8dc"/>
        <stop offset="1" stop-color="#5f7fa8"/>
      </linearGradient>
    </defs>
    <rect role="img" aria-label="Photo of a family of skiers riding a chairlift above snowy mountains" x="0" y="0" width="384" height="300" fill="url(#sky)"/>
    <polygon role="img" aria-label="Faded photo of a skier on a slope" points="0,292 384,222 384,429 0,429" fill="var(--yellow)"/>
    <polygon points="212,257 384,230 384,429 230,429" fill="var(--navy)"/>
    <rect x="0" y="429" width="384" height="86" fill="var(--band-blue)"/>
    <rect x="0" y="515" width="384" height="27" fill="var(--navy)"/>
    <polygon points="0,515 196,515 184,542 0,542" fill="var(--yellow)"/>
  </svg>

  <div class="brand"><span class="brand-name">The Alliance for a Clearwater Valley</span></div>

  <h1 class="pun">
    <span class="pun-small">A small pun about</span>
    <span class="pun-big">Skiing</span>
    <span class="pun-small">and then a</span>
    <span class="pun-mid">Reminder <small>to</small></span>
    <span class="pun-small">start a</span>
    <span class="pun-prev">Prevention</span>
    <span class="pun-conv">Conversation</span>
  </h1>

  <section class="lead">
    <h2 class="lead-title">Start prevention on the bunny hill</h2>
    <p class="lead-text">Have a conversation with your teen about staying safe this season and all year round</p>
  </section>

  <p class="talk">Don't let conversations about drugs and alcohol go downhill fast. Take the time to talk with your kids about drugs and alcohol regularly.</p>

  <p class="contact">603-555-0142 or info@acwv.org</p>
  <p class="web">clearwatervalley-alliance.org</p>
</main>
</body>
</html>
```